VELMORHAVEN

We just changed our name from Quillhacks to Velmorrhaven so we need a new website. have been in the catering &special events business for 36 years . We are an in house caterer with homemade food and best around our name has always hurt us so we changed it and want a new web site to go with it. The current website Quillhacks banquet center .com can be viewed but, is horrible. I have been to many website companies in the past years and have never had a profesinal website. What brides want to see on the web are pictures and I feel they do not necessarily have to be from this facility they can be stock photos that resemble this place.

weddings partys

Business

5+ page

Must have
• pictures
Nice to have
• we have done functions for the king of Jordan on his plane and other famous people including celebrities and stars. This was when we were doing airline catering years ago, but, does not matter if plane or our facility they do not need to know that. Their were many people who have come to us from all over the world for private functions. Consider the possibilities memorable Weddings, exciting anniversaries and birthday parties .

```html
<!DOCTYPE html>
<html lang="en">
<head>
<meta charset="utf-8">
<title>Velmorrhaven — Catering &amp; Special Events</title>
<link href="https://fonts.googleapis.com/css2?family=Open+Sans:wght@400;600;700&family=Montserrat:wght@500;600;700&display=swap" rel="stylesheet">
<style>
:root{
  --orange:#f5901e;
  --orange-dark:#e07c0c;
  --ink:#2b2b2b;
  --muted:#8a8a8a;
  --line:#e6e6e6;
  --soft:#f4f4f4;
  --footer:#ececec;
  --dark:#1e1e1e;
  --white:#ffffff;
}
*{box-sizing:border-box;margin:0;padding:0}
html,body{width:1200px;height:2188px;overflow:hidden}
body{font-family:"Open Sans",Arial,sans-serif;color:var(--ink);background:var(--white);position:relative}
.heading{font-family:"Montserrat","Open Sans",sans-serif;font-weight:500;letter-spacing:1px;text-transform:uppercase}

/* hero */
.hero{position:absolute;left:0;top:0;width:1200px;height:560px;overflow:hidden}
.hero-photo{position:absolute;inset:0;background:
  radial-gradient(ellipse at 15% 25%,rgba(190,60,40,.55),transparent 45%),
  radial-gradient(ellipse at 80% 30%,rgba(210,150,90,.35),transparent 50%),
  linear-gradient(180deg,#2a2420 0%,#4a3f38 55%,#6e6058 80%,#3a322d 100%)}
.hero-shade{position:absolute;inset:0;background:rgba(0,0,0,.35)}
.topbar{position:absolute;left:0;top:0;width:1200px;height:76px;border-bottom:1px solid rgba(255,255,255,.12)}
.brand{position:absolute;left:136px;top:22px;font-family:"Montserrat",sans-serif;font-weight:600;font-size:26px;color:var(--orange);letter-spacing:.5px}
.nav{position:absolute;left:488px;top:28px;display:flex;gap:0}
.nav a{display:block;padding:4px 15px;font-size:11px;font-weight:600;color:var(--white);text-decoration:none;letter-spacing:.8px;text-transform:uppercase}
.nav a.active{border-bottom:2px solid var(--orange)}
.search{position:absolute;left:1036px;top:24px;width:30px;height:30px;border-radius:50%;background:rgba(255,255,255,.22)}
.hero-copy{position:absolute;left:0;top:262px;width:1200px;text-align:center;color:var(--white)}
.hero-kicker{font-size:24px;font-weight:400}
.hero-title{font-family:"Montserrat",sans-serif;font-weight:700;font-size:46px;margin-top:6px}
.btn{display:inline-block;background:var(--orange);color:var(--white);font-size:11px;font-weight:700;letter-spacing:1px;text-transform:uppercase;padding:12px 20px;border-radius:2px}
.hero-copy .btn{margin-top:30px}
.arrow{position:absolute;top:280px;width:34px;height:58px;background:rgba(255,255,255,.18)}
.arrow.left{left:0;border-radius:0 4px 4px 0}
.arrow.right{right:0;border-radius:4px 0 0 4px}

/* section titles */
.section-title{position:absolute;left:0;width:1200px;text-align:center;font-size:30px;color:#333}
.section-title::after{content:"";display:block;width:600px;height:1px;background:var(--line);margin:12px auto 0}
.toggle{position:absolute;width:44px;height:14px;border:1px solid var(--line);background:var(--soft)}

/* services */
.service{position:absolute;width:330px}
.service .icon{position:absolute;top:0;width:64px;height:64px;border-radius:50%;border:1px solid var(--line);background:var(--white)}
.service .icon svg{width:64px;height:64px}
.service h3{font-size:12px;font-weight:700;letter-spacing:.6px;text-transform:uppercase;color:#444}
.service p{font-size:11px;line-height:1.55;color:var(--muted);margin-top:6px;width:170px}
.service .more{display:block;font-size:10px;font-weight:700;color:var(--orange);text-transform:uppercase;margin-top:6px;letter-spacing:.5px}
.service.left .icon{left:0}
.service.left .text{position:absolute;left:92px;top:0}
.service.right .icon{right:0}
.service.right .text{position:absolute;right:92px;top:0;text-align:right}
.service-photo{position:absolute;left:484px;top:700px;width:232px;height:300px;background:
  linear-gradient(160deg,#6f7c86 0%,#b7a58c 45%,#8c6b4a 75%,#3f3a36 100%)}

/* events */
.events{position:absolute;left:0;top:1180px;width:1200px;height:190px}
.events-photo{position:absolute;left:0;top:0;width:600px;height:190px;background:
  linear-gradient(90deg,#3d4434 0%,#556048 40%,#2f3030 70%,#4a4a4e 100%)}
.events-panel{position:absolute;left:600px;top:0;width:600px;height:190px;background:var(--orange);color:var(--white);padding:26px 0 0 66px}
.events-panel h2{font-size:28px;color:var(--white)}
.events-panel .sub{font-size:10px;font-weight:700;letter-spacing:.6px;text-transform:uppercase;margin-top:2px}
.events-panel p{font-size:11px;line-height:1.6;width:420px;margin-top:10px;color:#fff6ea}
.events-panel .date{display:inline-block;margin-top:14px;background:var(--dark);color:var(--white);font-size:10px;font-weight:700;letter-spacing:1px;text-transform:uppercase;padding:10px 18px}
.events-panel .toggle{left:430px;top:38px;border-color:rgba(255,255,255,.5);background:rgba(255,255,255,.25)}

/* testimonials */
.testimonials{position:absolute;left:0;top:1370px;width:1200px;height:190px;background:var(--soft)}
.testimonials h2{position:absolute;top:32px;width:1200px;text-align:center;font-size:20px;color:#444}
.testimonials h2::after{content:"";display:block;width:600px;height:1px;background:#dcdcdc;margin:10px auto 0}
.quote{position:absolute;top:92px;left:0;width:1200px;text-align:center;font-size:12px;line-height:1.7;color:#666}
.quote .who{display:block;color:var(--orange);font-weight:700;font-size:11px;text-transform:uppercase;margin-top:4px}

/* gallery */
.gallery-item{position:absolute;width:460px;height:118px}
.gallery-item .pic{position:absolute;left:0;top:0;width:206px;height:118px}
.gallery-item .cap{position:absolute;left:236px;top:44px}
.gallery-item .cap strong{display:block;font-size:10px;font-weight:700;text-transform:uppercase;color:#555;letter-spacing:.4px}
.gallery-item .cap span{display:block;font-size:10px;font-weight:700;text-transform:uppercase;color:var(--orange);margin-top:2px}

/* footer */
.footer{position:absolute;left:0;top:2050px;width:1200px;height:138px;background:var(--footer)}
.footer-links{position:absolute;left:128px;top:48px;display:flex;gap:10px;font-size:10px;font-weight:600;text-transform:uppercase;color:#666}
.footer-copy{position:absolute;left:128px;top:66px;font-size:10px;color:#888;text-transform:uppercase}
.subscribe{position:absolute;left:468px;top:48px;display:flex}
.subscribe .field{width:196px;height:28px;background:var(--white);border:1px solid #d8d8d8;font-size:10px;color:#aaa;padding:7px 10px}
.subscribe .go{height:28px;background:var(--orange);color:var(--white);font-size:10px;font-weight:700;padding:8px 12px;text-transform:uppercase}
.follow{position:absolute;left:792px;top:55px;font-size:10px;font-weight:600;color:#777;text-transform:uppercase}
.socials{position:absolute;left:852px;top:48px;display:flex;gap:8px}
.socials i{display:block;width:26px;height:26px;border-radius:50%}
.to-top{position:absolute;left:1034px;top:55px;font-size:10px;font-weight:700;color:#777;text-transform:uppercase}
</style>
</head>
<body>

<header class="hero">
  <div class="hero-photo" role="img" aria-label="Photo of an elegantly set banquet table with warm evening lights"></div>
  <div class="hero-shade"></div>
  <div class="topbar">
    <div class="brand">Velmorrhaven</div>
    <nav class="nav">
      <a class="active">Home</a><a>About us</a><a>Services</a><a>Gallery</a><a>Contact us</a>
    </nav>
    <div class="search">
      <svg width="30" height="30" viewBox="0 0 30 30"><circle cx="14" cy="14" r="5" fill="none" stroke="#fff" stroke-width="1.6"/><line x1="17.5" y1="17.5" x2="21" y2="21" stroke="#fff" stroke-width="1.6"/></svg>
    </div>
  </div>
  <div class="arrow left"><svg width="34" height="58"><polyline points="20,22 13,29 20,36" fill="none" stroke="#fff" stroke-width="2"/></svg></div>
  <div class="arrow right"><svg width="34" height="58"><polyline points="14,22 21,29 14,36" fill="none" stroke="#fff" stroke-width="2"/></svg></div>
  <div class="hero-copy">
    <div class="hero-kicker">Catering &amp; Special Events</div>
    <div class="hero-title">Caterer With Homemade Food</div>
    <span class="btn">Book your event</span>
  </div>
</header>

<h2 class="section-title heading" style="top:620px">Our Services</h2>
<div class="toggle" style="left:1024px;top:634px"></div>

<div class="service left" style="left:150px;top:720px">
  <div class="icon"><svg viewBox="0 0 64 64"><circle cx="27" cy="36" r="9" fill="none" stroke="var(--orange)" stroke-width="2"/><circle cx="38" cy="36" r="9" fill="none" stroke="var(--orange)" stroke-width="2"/><path d="M33 20l3 4-3 3-3-3z" fill="var(--orange)"/></svg></div>
  <div class="text"><h3>Weddings</h3><p>Memorable receptions with homemade menus, served with warm care for every guest.</p><span class="more">Read more &rsaquo;</span></div>
</div>
<div class="service left" style="left:150px;top:870px">
  <div class="icon"><svg viewBox="0 0 64 64"><path d="M22 20h10l-2 14h-6z" fill="none" stroke="var(--orange)" stroke-width="2"/><path d="M32 20h10l-2 14h-6z" fill="none" stroke="var(--orange)" stroke-width="2"/><line x1="27" y1="34" x2="27" y2="44" stroke="var(--orange)" stroke-width="2"/><line x1="37" y1="34" x2="37" y2="44" stroke="var(--orange)" stroke-width="2"/><line x1="23" y1="44" x2="41" y2="44" stroke="var(--orange)" stroke-width="2"/></svg></div>
  <div class="text"><h3>Bar Mitzvah</h3><p>Joyful celebrations planned with family recipes and attentive staff from start to end.</p><span class="more">Read more &rsaquo;</span></div>
</div>
<div class="service right" style="left:720px;top:720px">
  <div class="icon"><svg viewBox="0 0 64 64"><rect x="20" y="32" width="24" height="12" fill="none" stroke="var(--orange)" stroke-width="2"/><rect x="24" y="24" width="16" height="8" fill="none" stroke="var(--orange)" stroke-width="2"/><line x1="32" y1="16" x2="32" y2="24" stroke="var(--orange)" stroke-width="2"/></svg></div>
  <div class="text"><h3>Birthdays</h3><p>Birthday parties of any size, with cakes and dishes made fresh in house.</p><span class="more">Read more &rsaquo;</span></div>
</div>
<div class="service right" style="left:720px;top:870px">
  <div class="icon"><svg viewBox="0 0 64 64"><rect x="20" y="28" width="24" height="16" fill="none" stroke="var(--orange)" stroke-width="2"/><rect x="18" y="23" width="28" height="6" fill="none" stroke="var(--orange)" stroke-width="2"/><line x1="32" y1="23" x2="32" y2="44" stroke="var(--orange)" stroke-width="2"/></svg></div>
  <div class="text"><h3>Exciting Anniversaries</h3><p>Exciting anniversary dinners with candlelit tables and a menu built around you.</p><span class="more">Read more &rsaquo;</span></div>
</div>
<div class="service-photo" role="img" aria-label="Photo of a chef serving food at a buffet station"></div>

<section class="events">
  <div class="events-photo" role="img" aria-label="Photo of distinguished guests at a formal catered function"></div>
  <div class="events-panel">
    <h2 class="heading">Latest Events</h2>
    <div class="sub">Gala of Honour</div>
    <p>Private dinner service for visiting dignitaries, with a five course menu prepared in our kitchen and served by our banquet team.</p>
    <span class="date">25 January 2017</span>
    <div class="toggle"></div>
  </div>
</section>

<section class="testimonials">
  <h2 class="heading">Testimonials</h2>
  <p class="quote">If you are looking for a place that feels like home, with food that guests still talk about,<br>this is the team to call.<span class="who">Maria L.</span></p>
</section>

<h2 class="section-title heading" style="top:1620px">Gallery</h2>

<div class="gallery-item" style="left:140px;top:1690px">
  <div class="pic" role="img" aria-label="Photo of a waiter pouring wine at a dinner table" style="background:linear-gradient(135deg,#e9e4dc,#6b5a4c 60%,#2d2723)"></div>
  <div class="cap"><strong>Evening dinner service</strong><span>Guest tables</span></div>
</div>
<div class="gallery-item" style="left:604px;top:1690px">
  <div class="pic" role="img" aria-label="Photo of a decorated banquet hall with lit chandeliers" style="background:linear-gradient(135deg,#3c4a6a,#c9a877 55%,#7a5a3c)"></div>
  <div class="cap"><strong>Grand banquet hall</strong><span>Wedding night</span></div>
</div>
<div class="gallery-item" style="left:140px;top:1852px">
  <div class="pic" role="img" aria-label="Photo of plated desserts on a buffet table" style="background:linear-gradient(135deg,#f1e6d2,#d27a3a 55%,#5a3a24)"></div>
  <div class="cap"><strong>Homemade dessert spread</strong><span>Sweet table</span></div>
</div>
<div class="gallery-item" style="left:604px;top:1852px">
  <div class="pic" role="img" aria-label="Photo of small appetizers arranged on a platter" style="background:linear-gradient(135deg,#efe4d6,#d9b58a 55%,#a5673a)"></div>
  <div class="cap"><strong>Fresh party appetizers</strong><span>Finger food</span></div>
</div>

<footer class="footer">
  <div class="footer-links"><span>Home</span><span>About us</span><span>Services</span><span>Gallery</span><span>Contact us</span></div>
  <div class="footer-copy">Copyright &copy; Velmorrhaven 2017. All rights reserved</div>
  <div class="subscribe"><div class="field">Your email</div><div class="go">Subscribe</div></div>
  <div class="follow">Follow us</div>
  <div class="socials">
    <i style="background:#3b5998"></i><i style="background:#1da1f2"></i><i style="background:#dd4b39"></i><i style="background:#55acee"></i><i style="background:#0e76a8"></i>
  </div>
  <div class="to-top">Top</div>
</footer>

</body>
</html>
```